A Small Coastal town of New Zealand book!

we want a cool book cover for our book titled; Karewa Bay & The Wild Western Coasts - Old Tales, Boating, Hiking and sights to see...

attached are some screenshots of books we found that were similar to the topic i cover.

also attached are some screenshots of some ideas i have been playing with my self with myself on canva...

i quite like the first one how he managed to put 5 images there without making it look too busy...

Target Market(s)

Tourists

Industry/Entity Type

Tourism

Font styles to use
Serif
Sans Serif

Requirements
Must have
• Nice coastal image and good fonts and text placement
Should not have
• not to busy...

```html
<!DOCTYPE html>
<html lang="en">
<head>
<meta charset="utf-8">
<title>Karewa Bay &amp; The Wild Western Coasts — Book Cover</title>
<link rel="stylesheet" href="https://fonts.googleapis.com/css2?family=Playfair+Display:ital,wght@0,400;1,400&family=Libre+Baskerville:ital,wght@0,400;1,400&display=swap">
<style>
  :root {
    --white: #ffffff;
    --ink: #2b3a33;
    --label-bg: rgba(236, 240, 236, 0.78);
    --forest-dark: #2f5a22;
    --forest: #5f8c34;
    --forest-light: #8db24e;
    --sand: #f1efe8;
    --rock: #5d6664;
    --shallows: #5fc7c0;
    --sea: #1c8f93;
    --sea-deep: #0d5c66;
  }
  * { margin: 0; padding: 0; box-sizing: border-box; }
  html, body { width: 759px; height: 1200px; overflow: hidden; background: #ffffff; }
  .cover {
    position: relative;
    width: 759px;
    height: 1200px;
    overflow: hidden;
    color: var(--white);
  }
  .cover-photo {
    position: absolute;
    inset: 0;
    background:
      radial-gradient(ellipse 380px 260px at 620px 980px, rgba(93,102,100,0.55), transparent 70%),
      linear-gradient(150deg,
        transparent 0%, transparent 63%,
        var(--sand) 66%, var(--sand) 71%,
        var(--shallows) 74%, var(--sea) 84%, var(--sea-deep) 100%),
      linear-gradient(160deg,
        var(--forest-dark) 0%, var(--forest) 28%, var(--forest-light) 45%,
        var(--forest) 60%, var(--forest-dark) 75%);
  }
  .rule {
    position: absolute;
    left: 296px;
    width: 152px;
    height: 4px;
    background: var(--white);
  }
  .rule--top { top: 64px; }
  .rule--bottom { top: 1142px; }
  .title {
    position: absolute;
    top: 82px;
    left: 0;
    width: 100%;
    text-align: center;
    font-family: "Playfair Display", Georgia, serif;
    font-style: italic;
    font-weight: 400;
    font-size: 106px;
    line-height: 1.1;
    letter-spacing: 1px;
  }
  .subtitle {
    position: absolute;
    top: 232px;
    left: 0;
    width: 100%;
    text-align: center;
    font-family: "Libre Baskerville", Georgia, serif;
    font-size: 25px;
  }
  .topic {
    position: absolute;
    display: flex;
    align-items: center;
    justify-content: center;
    height: 66px;
    background: var(--label-bg);
    color: var(--ink);
    font-family: "Libre Baskerville", Georgia, serif;
    font-style: italic;
    font-size: 28px;
  }
  .topic--history { top: 354px; left: 230px; width: 284px; }
  .topic--hiking  { top: 574px; left: 296px; width: 218px; }
  .topic--sights  { top: 804px; left: 197px; width: 365px; }
  .author-tag {
    position: absolute;
    top: 936px;
    left: 0;
    width: 100%;
    text-align: center;
    font-family: "Libre Baskerville", Georgia, serif;
    font-size: 19px;
    letter-spacing: 6px;
  }
  .author-name {
    position: absolute;
    top: 962px;
    left: 0;
    width: 100%;
    text-align: center;
    font-family: "Playfair Display", Georgia, serif;
    font-style: italic;
    font-size: 80px;
    line-height: 76px;
  }
</style>
</head>
<body>
  <main class="cover">
    <div class="cover-photo" role="img" aria-label="Aerial photograph of a bush-covered headland meeting a white sand beach, dark rocks and turquoise sea"></div>
    <div class="rule rule--top"></div>
    <h1 class="title">Karewa Bay</h1>
    <p class="subtitle">&amp; The Wild Western Coasts</p>
    <p class="topic topic--history">old tales</p>
    <p class="topic topic--hiking">hiking</p>
    <p class="topic topic--sights">and sights to see</p>
    <p class="author-tag">BEST SELLING AUTHOR</p>
    <p class="author-name">Liam<br>Hartwell</p>
    <div class="rule rule--bottom"></div>
  </main>
</body>
</html>
```